Paraffin Wax Packaging Design for Nail and Beauty Industry

We need an attractive design for the packaging of our new product, Paraffin Wax. Our company is a wholesale beauty/nail supply company that has been selling to nail salons in the US market for 10 years. We currently sell this product that we buy from another company. Now we want to launch our own brand of Paraffin Wax.

Target Market(s)

Retail nail salons in the US market.

Industry/Entity Type

Industry

Font styles to use
Sans Serif

Colors

Designer to choose colors to be used in the design.

Requirements
Must have
• Our logo (attached).
• All information on the "Ingredient List" (attached).
• Design for Clear Packaging so product can show through.
• Design for Package Dimensions of 4.25" x 11" (110cm x 280 cm).
Nice to have
• Picture related to women's skin and or beauty.
• Contrast as in the design of product that we currently sell (attached).

```html
<!DOCTYPE html>
<html lang="en">
<head>
<meta charset="UTF-8">
<title>Paraffin Wax Package</title>
<link rel="stylesheet" href="https://fonts.googleapis.com/css2?family=Montserrat:wght@700&family=Source+Sans+3:wght@400;600;700&display=swap">
<style>
  :root {
    --navy: #0a1f5c;
    --cyan: #0a8fcf;
    --pouch: #e3e3e4;
    --ink: #2a2585;
    --white: #ffffff;
    --page: #ffffff;
  }
  * { margin: 0; padding: 0; box-sizing: border-box; }
  html, body {
    width: 1200px; height: 1200px; overflow: hidden;
    background: var(--page);
    font-family: "Source Sans 3", "Segoe UI", Arial, sans-serif;
  }
  .package {
    position: absolute;
    left: 416px; top: 120px;
    width: 366px; height: 958px;
    background: var(--pouch);
    overflow: hidden;
  }
  .band-top {
    position: absolute; left: 0; top: 0;
    width: 100%; height: 300px;
    background: linear-gradient(180deg, var(--navy) 0%, var(--navy) 62%, var(--cyan) 100%);
  }
  .band-bottom {
    position: absolute; left: 0; bottom: 0;
    width: 100%; height: 150px;
    background: linear-gradient(180deg, var(--cyan) 0%, var(--navy) 30%, var(--navy) 100%);
  }
  .product-title {
    position: absolute;
    top: 16px; left: 0; width: 100%;
    text-align: center;
    color: var(--white);
    font-family: "Montserrat", "Segoe UI", Arial, sans-serif;
    font-weight: 700;
    font-size: 52px;
    line-height: 54px;
  }
  .copy {
    position: absolute;
    left: 51px; width: 259px;
    top: 308px;
    color: var(--ink);
    font-size: 17.5px;
    line-height: 20.8px;
  }
  .copy p { margin-bottom: 20.8px; }
  .copy .line {
    display: block;
    white-space: nowrap;
    text-align: justify;
    text-align-last: justify;
  }
  .copy .line.end { text-align-last: center; }
  .copy .claim { font-weight: 600; }
  .copy .label { font-weight: 700; }
  .brand-name {
    position: absolute;
    top: 664px; left: 0; width: 100%;
    text-align: center;
    color: var(--ink);
    font-weight: 600;
    font-size: 34px;
  }
  .net-weight {
    position: absolute;
    right: 24px; bottom: 14px;
    color: var(--white);
    font-weight: 700;
    font-size: 17px;
  }
</style>
</head>
<body>
  <div class="package">
    <div class="band-top" role="img" aria-label="Navy and cyan decorative wave band"></div>
    <div class="band-bottom" role="img" aria-label="Navy and cyan decorative wave band"></div>

    <h1 class="product-title">PARAFFIN<br>WAX</h1>

    <div class="copy">
      <p class="claim">
        <span class="line">Compatible for use with most</span>
        <span class="line">wax paraffin heat therapy</span>
        <span class="line end">units.</span>
      </p>
      <p class="claim">
        <span class="line">Deeply Moisturizes the Skin</span>
        <span class="line">Restoring a Healthier Look and</span>
        <span class="line end">Feel to Skin.</span>
      </p>
      <p>
        <span class="line"><span class="label">Ingredients:</span> Paraffin waxes and</span>
        <span class="line">Hydrocarbon waxes, Petrolatum,</span>
        <span class="line">Paraffin oils, Apricot kernel oil,</span>
        <span class="line end">Fragrance D &amp; C dyes.</span>
      </p>
      <p>
        <span class="line"><span class="label">Caution:</span> Paraffin is flammable.</span>
        <span class="line">Do not use near open flame or</span>
        <span class="line">an unprotected resistance</span>
        <span class="line end">heater.</span>
      </p>
    </div>

    <div class="brand-name">By Marisol</div>

    <div class="net-weight">Net Wt. 1 lb. (450 g.)</div>
  </div>
</body>
</html>
```